After-School Program - End of the Year Mailing to Donors

We would like to highlight some of our accomplishments from the year and ask people to donate to our organization. We are a non-profit organization that serves underprivileged children with after school programs. We want a 6x9 flyer with printing on both sides that we can mail out soon. The flyer should be a mix of great photos, some text, and a space for mailing and return address.

Target Market(s)

regular donors

Industry/Entity Type

Education

Font styles to use
Serif

Colors

Designer to choose colors to be used in the design.

Requirements
Must have
• Photos, text, a space on one side for a mailing label, a return address, and a stamp.
Nice to have
• attractive, eye-catching
Should not have
• boring

```html
<!DOCTYPE html>
<html lang="en">
<head>
<meta charset="utf-8">
<title>Hillcrest Family Learning Center – Donor Postcard</title>
<link href="https://fonts.googleapis.com/css2?family=Ubuntu:wght@500&family=PT+Sans:wght@400;700&display=swap" rel="stylesheet">
<style>
  :root{
    --backdrop:#b7b8ba;
    --orange-deep:#d9780d;
    --orange:#ee9a16;
    --gold:#f7c21a;
    --yellow:#ffe500;
    --ink:#1b1b1b;
    --white:#ffffff;
    --paper:#f6f0f3;
    --rule:#c9c3c6;
  }
  *{box-sizing:border-box;margin:0;padding:0}
  html,body{width:912px;height:1200px;overflow:hidden;background:var(--backdrop)}
  .card{position:absolute;left:116px;width:680px;height:453px;overflow:hidden;
        box-shadow:0 4px 10px rgba(0,0,0,.35);font-family:"PT Sans",sans-serif;color:var(--ink)}
  .card--front{top:92px}
  .card--back{top:640px;background:var(--paper)}
  .card svg.card__art{position:absolute;inset:0;width:100%;height:100%}

  .org-mark{position:absolute;background:var(--white);box-shadow:2px 2px 4px rgba(0,0,0,.3);
            display:flex;flex-direction:column;align-items:center;justify-content:center;gap:8px;text-align:center;
            font-family:"Ubuntu",sans-serif;font-weight:500;color:var(--ink)}
  .org-mark__square{width:30px;height:30px;background:var(--ink)}
  .card--front .org-mark{left:26px;top:0;width:127px;height:162px;font-size:13px;line-height:1.25;padding:0 10px}
  .card--back .org-mark{left:442px;top:0;width:90px;height:114px;font-size:10px;line-height:1.2;padding:0 6px}
  .card--back .org-mark__square{width:22px;height:22px}

  .front__title{position:absolute;left:472px;top:34px;width:200px;font-family:"Ubuntu",sans-serif;font-weight:500;
                font-size:21px;line-height:24px;letter-spacing:1px;color:var(--white);text-transform:uppercase}
  .front__tagline{position:absolute;left:472px;top:122px;width:200px;font-family:"Ubuntu",sans-serif;font-weight:500;
                  font-size:15.5px;line-height:19px;letter-spacing:.6px;color:var(--white)}
  .front__url{position:absolute;left:491px;top:417px;font-family:"Ubuntu",sans-serif;font-weight:500;font-size:12px;
              letter-spacing:1.5px;color:var(--ink)}

  .back__title{position:absolute;left:24px;top:26px;font-family:"Ubuntu",sans-serif;font-weight:500;font-size:24px;
               line-height:28px;letter-spacing:.5px;color:var(--ink);text-transform:uppercase}
  .back__appeal{position:absolute;left:24px;top:92px;width:290px;font-size:12.2px;line-height:17px}
  .back__appeal strong{font-weight:700}
  .return-address{position:absolute;left:24px;top:350px;display:flex;gap:16px;align-items:flex-start}
  .return-address__square{width:44px;height:44px;border:3px solid var(--ink);margin-top:4px}
  .return-address address{font-style:normal;font-weight:700;font-size:10.5px;line-height:14.6px}

  .stamp-box{position:absolute;left:576px;top:20px;width:83px;height:94px;background:var(--white);
             border:1px solid var(--rule);display:flex;align-items:center;justify-content:center;text-align:center;
             font-size:11px;line-height:20px}
  .mail-lines{position:absolute;left:442px;top:195px;width:218px;list-style:none}
  .mail-lines li{height:38px;border-top:1px solid var(--rule)}
  .social{position:absolute;left:497px;top:385px;width:84px;height:27px;border:1.5px solid #3b5998;background:var(--white);
          display:flex;align-items:center;gap:5px;padding:0 5px;font-size:9px;font-weight:700;color:#3b5998}
  .social__square{width:14px;height:14px;background:#3b5998;flex:none}
  .social-hint{position:absolute;left:439px;top:418px;width:200px;text-align:center;font-size:8px}
</style>
</head>
<body>

<section class="card card--front" aria-label="Postcard front">
  <svg class="card__art" viewBox="0 0 680 453" aria-hidden="false">
    <defs>
      <linearGradient id="photoTones" x1="0" y1="0" x2="0" y2="1">
        <stop offset="0" stop-color="#7f9a6a"/><stop offset=".5" stop-color="#6b6f7e"/><stop offset="1" stop-color="#3e4351"/>
      </linearGradient>
      <linearGradient id="panelOrange" x1="1" y1="0" x2="0" y2="1">
        <stop offset="0" stop-color="var(--orange-deep)"/><stop offset=".55" stop-color="var(--orange)"/><stop offset="1" stop-color="var(--gold)"/>
      </linearGradient>
      <linearGradient id="portraitTones" x1="0" y1="0" x2="0" y2="1">
        <stop offset="0" stop-color="#6d7aa8"/><stop offset="1" stop-color="#c8262b"/>
      </linearGradient>
      <linearGradient id="musicTones" x1="0" y1="0" x2="0" y2="1">
        <stop offset="0" stop-color="#b9c7a8"/><stop offset="1" stop-color="#6b5a45"/>
      </linearGradient>
      <linearGradient id="outdoorTones" x1="0" y1="0" x2="0" y2="1">
        <stop offset="0" stop-color="#7ea3c7"/><stop offset="1" stop-color="#5f8a45"/>
      </linearGradient>
    </defs>
    <rect role="img" aria-label="Group photo of smiling children with a volunteer in a park" x="0" y="0" width="460" height="453" fill="url(#photoTones)"/>
    <path d="M373,0 C450,110 480,280 364,453 L680,453 L680,0 Z" fill="url(#panelOrange)"/>
    <path d="M373,0 C450,110 480,280 364,453" fill="none" stroke="var(--ink)" stroke-width="9"/>
    <path d="M369,0 C445,110 475,280 359,453" fill="none" stroke="var(--white)" stroke-width="4"/>
    <g role="img" aria-label="Portrait of a smiling girl wearing a red jacket and a costume headband">
      <circle cx="390" cy="334" r="92" fill="var(--ink)"/><circle cx="390" cy="334" r="89" fill="var(--white)"/>
      <circle cx="390" cy="334" r="85" fill="url(#portraitTones)"/>
    </g>
    <g role="img" aria-label="Students playing violin and cello at a music lesson">
      <circle cx="523" cy="291" r="62" fill="var(--ink)"/><circle cx="523" cy="291" r="59.5" fill="var(--white)"/>
      <circle cx="523" cy="291" r="56" fill="url(#musicTones)"/>
    </g>
    <g role="img" aria-label="Children sitting together outdoors">
      <circle cx="640" cy="288" r="38" fill="var(--ink)"/><circle cx="640" cy="288" r="36" fill="var(--white)"/>
      <circle cx="640" cy="288" r="33" fill="url(#outdoorTones)"/>
    </g>
    <g role="img" aria-label="Two boys posing on a playground">
      <circle cx="593" cy="352" r="48" fill="var(--ink)"/><circle cx="593" cy="352" r="45.5" fill="var(--white)"/>
      <circle cx="593" cy="352" r="42" fill="url(#outdoorTones)"/>
    </g>
  </svg>

  <div class="org-mark"><span class="org-mark__square"></span>Hillcrest Family Learning Center</div>
  <h1 class="front__title">Hillcrest Family Learning Center</h1>
  <p class="front__tagline">Educational And Community-Building Programs For Children, Youth And Families</p>
  <p class="front__url">www.brightpathkids.org</p>
</section>

<section class="card card--back" aria-label="Postcard back">
  <svg class="card__art" viewBox="0 0 680 453">
    <defs>
      <linearGradient id="backPanel" x1="0" y1="0" x2="1" y2="0">
        <stop offset="0" stop-color="var(--yellow)"/><stop offset=".45" stop-color="var(--gold)"/><stop offset="1" stop-color="var(--orange)"/>
      </linearGradient>
      <linearGradient id="fadedPortrait" x1="0" y1="0" x2="0" y2="1">
        <stop offset="0" stop-color="#ece8ee"/><stop offset="1" stop-color="#f3dde5"/>
      </linearGradient>
      <linearGradient id="eventTones" x1="0" y1="0" x2="0" y2="1">
        <stop offset="0" stop-color="#5a5f72"/><stop offset="1" stop-color="#a0474f"/>
      </linearGradient>
      <linearGradient id="groupTones" x1="0" y1="0" x2="0" y2="1">
        <stop offset="0" stop-color="#9bb4cf"/><stop offset=".5" stop-color="#6d6560"/><stop offset="1" stop-color="#4f7a3c"/>
      </linearGradient>
    </defs>
    <rect role="img" aria-label="Faded portrait of a smiling girl behind the mailing area" x="380" y="0" width="300" height="453" fill="url(#fadedPortrait)"/>
    <path d="M0,0 L342,0 C420,120 420,320 350,453 L0,453 Z" fill="url(#backPanel)"/>
    <path d="M342,0 C420,120 420,320 350,453" fill="none" stroke="var(--ink)" stroke-width="9"/>
    <path d="M348,0 C426,120 426,320 356,453" fill="none" stroke="var(--white)" stroke-width="4"/>
    <g role="img" aria-label="Two girls in party crowns at a celebration">
      <circle cx="364" cy="62" r="58" fill="var(--ink)"/><circle cx="364" cy="62" r="55.5" fill="var(--white)"/>
      <circle cx="364" cy="62" r="52" fill="url(#eventTones)"/>
    </g>
    <g role="img" aria-label="Children and staff gathered in a courtyard">
      <circle cx="368" cy="171" r="58" fill="var(--ink)"/><circle cx="368" cy="171" r="55.5" fill="var(--white)"/>
      <circle cx="368" cy="171" r="52" fill="url(#groupTones)"/>
    </g>
    <g role="img" aria-label="Kids in hats cheering at an outdoor event">
      <circle cx="369" cy="278" r="58" fill="var(--ink)"/><circle cx="369" cy="278" r="55.5" fill="var(--white)"/>
      <circle cx="369" cy="278" r="52" fill="url(#eventTones)"/>
    </g>
    <g role="img" aria-label="Large group of students on a field with hills behind">
      <circle cx="334" cy="383" r="58" fill="var(--ink)"/><circle cx="334" cy="383" r="55.5" fill="var(--white)"/>
      <circle cx="334" cy="383" r="52" fill="url(#groupTones)"/>
    </g>
  </svg>

  <h2 class="back__title">Hillcrest Family<br>Learning Center</h2>
  <p class="back__appeal">Hillcrest Family Learning Center is in the middle of its <strong>24th year of ministry</strong> and we need your help to finish our year strong! We need another <strong>$35,000</strong> from our individual donors to help us meet our budget. We serve over <strong>150 children</strong> each day at our four sites with a unique mix of homework help, a focus on literacy, enrichment classes - including music lessons, and a caring environment based on God’s love. Please help us continue to impact children and families through our high quality faith-based educational programs. To contribute, please visit www.brightpathkids.org and click on the donate button.</p>

  <div class="return-address">
    <span class="return-address__square"></span>
    <address>Hillcrest Family Learning Center<br>218 N. Maple Grove Ave.<br>Fairview, CA 90210<br>(555) 014-2277<br>www.brightpathkids.org</address>
  </div>

  <div class="org-mark"><span class="org-mark__square"></span>Hillcrest Family Learning Center</div>
  <div class="stamp-box">Please<br>place<br>stamp<br>here</div>
  <ul class="mail-lines"><li></li><li></li><li></li><li></li><li></li></ul>
  <div class="social"><span class="social__square"></span>Find us online</div>
  <p class="social-hint">search Hillcrest Family Learning Center</p>
</section>

</body>
</html>
```